Trucking company specializing in intermodal containers

We need a logo design for our trucking company based in Kent, Washington. Our companies name is Dorvale Haulworks LLC, we specialize in intermodal containers, and work off of the Crestmark rail lines and the ports. We provide service by transporting freight with our fleet of trucks. We operate within Washington, Oregon, and Idaho. Our fleet consists of an east division and a local division. Our team motto currently is globally connected, locally invested.

Target Market(s)

brokers, intermodal management companies, customers

Industry/Entity Type

Trucking Company

Contact Information for Business Card

physical address 4519 N. 163rd Pl Kent, WA 98517
office number is 253-614-9026

Font styles to use
Sans Serif

Colors

Designer to choose colors to be used in the design.

Requirements
Must have
• We need to update our current logo. Something like an emblem; that makes a statement that this logo/ sign represents Dorvale Haulworks. Something like a royal stamp but in this case a royal shield.
Nice to have
• simple, yet bold. something someone does not currently have. We need something fresh and exciting. Something that will also make a statement because currently our reputation is great within the industry and our community. But we need to reflect that we are professional and willing to provide the best service. We are open to new statement lines.
Should not have
• Should not have something thats been used before. We are open to suggestions that you have and a design that is completely unique and you make originally without what we want but what you like as well. Ofcourse it should still represent the industry we are in.

```html
<!DOCTYPE html>
<html lang="en">
<head>
<meta charset="utf-8">
<title>Dorvale Haulworks LLC — Business Card</title>
<link rel="stylesheet" href="https://fonts.googleapis.com/css2?family=Arimo:wght@400;700&display=swap">
<style>
  :root {
    --page-bg: #e6e6e6;
    --card-front-top: #d2d2d2;
    --card-front-bottom: #a9a9a9;
    --card-back-top: #f1f1f1;
    --card-back-bottom: #dcdcdc;
    --swoosh-light: #9a9a9a;
    --swoosh-dark: #555555;
    --brand-red: #8b2a26;
    --ink: #1d1d1d;
    --faded: #8c8c8c;
    --rule: #c4c4c4;
  }
  * { box-sizing: border-box; margin: 0; padding: 0; }
  html, body { width: 1200px; height: 869px; overflow: hidden; }
  body {
    background: var(--page-bg);
    font-family: "Arimo", Arial, sans-serif;
    display: flex;
    align-items: center;
    justify-content: center;
    gap: 60px;
  }
  .card {
    position: relative;
    width: 520px;
    height: 297px;
    overflow: hidden;
    box-shadow: 0 4px 14px rgba(0,0,0,0.18);
  }
  .card-front { background: linear-gradient(160deg, var(--card-front-top), var(--card-front-bottom)); }
  .card-back { background: linear-gradient(160deg, var(--card-back-top), var(--card-back-bottom)); }
  .swoosh { position: absolute; left: 0; bottom: 0; width: 520px; height: 297px; }
  .front-brand {
    position: absolute;
    left: 0; right: 0; top: 58px;
    display: flex;
    align-items: center;
    justify-content: center;
    gap: 18px;
  }
  .brand-mark {
    flex: none;
    width: 64px;
    height: 64px;
    border-radius: 50%;
    background: var(--brand-red);
  }
  .brand-name {
    font-weight: 700;
    font-size: 42px;
    line-height: 1.08;
    color: var(--brand-red);
    letter-spacing: 0.5px;
  }
  .back-content {
    position: absolute;
    left: 0; right: 0; top: 34px;
    text-align: center;
  }
  .back-name {
    font-weight: 700;
    font-size: 26px;
    color: var(--faded);
  }
  .back-rule {
    width: 300px;
    height: 1px;
    margin: 12px auto 16px;
    background: var(--rule);
  }
  .contact-label { font-size: 15px; color: var(--brand-red); }
  .contact-value { font-size: 17px; color: var(--ink); margin-bottom: 12px; margin-top: 2px; }
</style>
</head>
<body>
  <section class="card card-front">
    <svg class="swoosh" viewBox="0 0 520 297" aria-hidden="true">
      <defs>
        <linearGradient id="swooshFront" x1="0" y1="0" x2="1" y2="0">
          <stop offset="0" stop-color="var(--swoosh-light)"/>
          <stop offset="1" stop-color="var(--swoosh-dark)"/>
        </linearGradient>
      </defs>
      <path d="M0,297 L0,250 Q280,300 520,160 L520,297 Z" fill="url(#swooshFront)"/>
    </svg>
    <div class="front-brand">
      <span class="brand-mark"></span>
      <span class="brand-name">Dorvale<br>Haulworks LLC</span>
    </div>
  </section>

  <section class="card card-back">
    <svg class="swoosh" viewBox="0 0 520 297" aria-hidden="true">
      <defs>
        <linearGradient id="swooshBack" x1="0" y1="0" x2="1" y2="0">
          <stop offset="0" stop-color="var(--swoosh-light)"/>
          <stop offset="1" stop-color="var(--swoosh-dark)"/>
        </linearGradient>
      </defs>
      <path d="M0,297 L0,272 Q300,305 520,190 L520,297 Z" fill="url(#swooshBack)"/>
    </svg>
    <div class="back-content">
      <div class="back-name">Dorvale Haulworks LLC</div>
      <div class="back-rule"></div>
      <div class="contact-label">Physical Address</div>
      <div class="contact-value">4519 N. 163rd Pl Kent, WA 98517</div>
      <div class="contact-label">Office number</div>
      <div class="contact-value">253-614-9026</div>
    </div>
  </section>
</body>
</html>
```